Lifestyle blog needs a website

I have a blog called Kite and Compass. Logo has been done and I also have the wordpress site with a theme already added to it.

The basics are there but I need design expertise to put everything together, make it look great and ready for me to go and in and start using. Basically what is there at the moment needs to be deleted and start again (not a lot - just me playing around). I am not attached to the theme and am happy to go with whatever ideas you can come up with. At the moment I am looking at 3 lifestyle categories (Fashion, Fitness, Feelings) with a contact page so not an extensive build.

Audience will be women over 40 but please don't make this 'frumpy' - it is aimed at the women who act, look and feel younger than their age and so 'pink & fluffy' and 'old & solid' is not the look I am going for.

My deepest apologies for the delay in responding to designs. I had a family matter which took meant I was unable to spend the quality time required to review. I will therefore be reviewing and deciding over this weekend. Once again, my sincere apologies.

Women over 40

• Feeling of being targeted at old market

```html
<!DOCTYPE html>
<html lang="en">
<head>
<meta charset="utf-8">
<title>Kite and Compass — Lifestyle Blog</title>
<link href="https://fonts.googleapis.com/css2?family=Open+Sans:wght@400;600;700&display=swap" rel="stylesheet">
<style>
  :root{
    --brand-red:#d1353d;
    --brand-red-dark:#b92a31;
    --ink:#222222;
    --white:#ffffff;
    --overlay:rgba(38,38,40,0.78);
    --hero-top:#8a8f97;
    --hero-bottom:#3c3a3b;
  }
  *{box-sizing:border-box;margin:0;padding:0}
  html,body{width:843px;height:1200px;overflow:hidden;background:var(--white)}
  body{font-family:"Open Sans",Arial,sans-serif;color:var(--ink)}
  .page{position:relative;width:843px;height:1200px;overflow:hidden}

  /* Header */
  .site-header{position:absolute;left:0;top:0;width:843px;height:70px;background:var(--white)}
  .brand{position:absolute;left:16px;top:14px;display:flex;align-items:center;gap:8px;
    color:var(--brand-red);font-weight:700;font-size:22px;line-height:1}
  .brand-dot{width:14px;height:14px;border-radius:50%;background:var(--brand-red)}
  .main-nav{position:absolute;right:20px;top:26px;display:flex;gap:10px;font-size:12px;font-weight:600;letter-spacing:.3px}
  .main-nav a{color:var(--ink);text-decoration:none}
  .main-nav a.is-active{color:var(--brand-red);border-bottom:2px solid var(--brand-red);padding-bottom:2px}

  /* Hero */
  .hero{position:absolute;left:0;top:70px;width:843px;height:346px;
    background:linear-gradient(180deg,var(--hero-top) 0%,#6f6a6b 45%,var(--hero-bottom) 100%)}
  .welcome{position:absolute;left:0;top:155px;width:464px;height:191px;background:var(--overlay);
    color:var(--white);text-align:center;padding:24px 28px}
  .welcome h1{font-size:32px;font-weight:400;letter-spacing:1px;margin-bottom:10px}
  .welcome p{font-size:12.5px;line-height:1.45}
  .newsletter{position:absolute;left:472px;top:85px;width:348px;height:253px;background:var(--brand-red);
    color:var(--white);text-align:center;padding:18px 24px}
  .newsletter h2{font-size:23px;font-weight:400;line-height:1.25;margin-bottom:8px}
  .newsletter p{font-size:12.5px;line-height:1.4;margin-bottom:18px}
  .email-field{display:block;width:232px;height:36px;margin:0 auto 12px;background:var(--white);
    color:#9a9a9a;font-size:13px;line-height:36px}
  .subscribe-btn{display:block;width:154px;height:38px;margin:0 auto;border:2px solid var(--white);
    font-size:18px;line-height:34px;letter-spacing:.5px}

  /* Posts */
  .posts-title{position:absolute;left:0;top:452px;width:843px;text-align:center;color:var(--brand-red);
    font-size:38px;font-weight:400}
  .post-card{position:absolute;overflow:hidden}
  .post-card .media{position:absolute;inset:0}
  .post-label{position:absolute;left:0;bottom:18px;background:var(--brand-red);color:var(--white);
    font-size:24px;padding:4px 14px 6px;width:75%}
  .post-1{left:22px;top:525px;width:192px;height:192px}
  .post-1 .media{background:linear-gradient(160deg,#c9b9a8,#6b5a4e)}
  .post-2{left:244px;top:525px;width:192px;height:192px;background:var(--brand-red);color:var(--white);text-align:center;padding-top:52px}
  .post-2 h3{font-size:24px;font-weight:400;margin-bottom:6px}
  .post-2 p{font-size:10px;line-height:1.3;padding:0 38px}
  .post-3{left:22px;top:736px;width:192px;height:191px}
  .post-3 .media{background:linear-gradient(160deg,#f2c6dd,#e49bc6)}
  .post-4{left:244px;top:736px;width:192px;height:191px}
  .post-4 .media{background:linear-gradient(160deg,#5b5b60,#cfcac4)}
  .post-featured{left:469px;top:525px;width:351px;height:402px}
  .post-featured .media{background:linear-gradient(180deg,#f3b33c 0%,#e07b25 45%,#5a3417 100%)}
  .post-featured .post-label{bottom:42px;width:74%;font-size:27px;padding:16px 14px 18px}

  /* Footer */
  .site-footer{position:absolute;left:0;top:955px;width:843px;height:245px;background:var(--brand-red);color:var(--white)}
  .author-photo{position:absolute;left:34px;top:15px;width:100px;height:100px;border-radius:50%;
    background:radial-gradient(circle,#7a7a7a,#2f2f2f);border:3px solid var(--white)}
  .footer-intro{position:absolute;left:150px;top:22px;width:370px;text-align:center;font-size:14px;font-weight:600;line-height:1.45}
  .footer-links{position:absolute;left:690px;top:24px;width:120px;text-align:center;list-style:none;font-size:16px;line-height:1.3}
  .social{position:absolute;left:38px;top:155px;display:flex;gap:32px}
  .social span{width:34px;height:34px;border-radius:50%;background:var(--white)}
  .copyright{position:absolute;left:0;bottom:0;width:843px;height:36px;background:var(--brand-red-dark);
    text-align:center;font-size:11px;line-height:36px}
</style>
</head>
<body>
<div class="page">
  <header class="site-header">
    <div class="brand"><span class="brand-dot"></span>Kite and Compass</div>
    <nav class="main-nav">
      <a class="is-active" href="#">HOME</a>
      <a href="#">FASHION</a>
      <a href="#">FITNESS</a>
      <a href="#">FEELINGS</a>
      <a href="#">CONTACT</a>
    </nav>
  </header>

  <section class="hero" role="img" aria-label="Photo of a woman against a mountain landscape">
    <div class="welcome">
      <h1>WELCOME!</h1>
      <p>Lorem ipsum dolor sit amet, consectetur adipiscing elit. Aenean et amet ligula vitae enim consequat sodales. Nullam et amet condimentum enim. Praesent auctor eros nec feugiat scelerisque. Curabitur a ipsum tincidunt lacus viverra facilisis. Nunc tincidunt ligula eu metus volutpat, sed blandit nisi imperdiet. Maecenas eget varius justo.</p>
    </div>
    <div class="newsletter">
      <h2>SUBSCRIBE TO<br>OUR NEWSLETTER</h2>
      <p>Lorem ipsum dolor sit amet, consectetur adipiscing elit. Aenean sit amet ligula vitae enim consequat sodales.</p>
      <span class="email-field">Enter your email here</span>
      <span class="subscribe-btn">SUBSCRIBE</span>
    </div>
  </section>

  <h2 class="posts-title">Posts</h2>

  <article class="post-card post-1">
    <div class="media" role="img" aria-label="Photo of clothes on a rail"></div>
    <div class="post-label">Post 1</div>
  </article>
  <article class="post-card post-2">
    <h3>Post 2</h3>
    <p>Brief description where the reader gets over the post</p>
  </article>
  <article class="post-card post-3">
    <div class="media" role="img" aria-label="Photo of a green smoothie on a pink table"></div>
    <div class="post-label">Post 3</div>
  </article>
  <article class="post-card post-4">
    <div class="media" role="img" aria-label="Photo of a laptop and notebook on a desk"></div>
    <div class="post-label">Post 4</div>
  </article>
  <article class="post-card post-featured">
    <div class="media" role="img" aria-label="Photo of a yoga pose silhouetted at sunset by the sea"></div>
    <div class="post-label">Featured content</div>
  </article>

  <footer class="site-footer">
    <div class="author-photo" role="img" aria-label="Author portrait"></div>
    <p class="footer-intro">Lorem ipsum dolor sit amet, consectetur adipiscing elit. Aenean sit amet ligula vitae enim consequat sodales.</p>
    <ul class="footer-links">
      <li>links:</li>
      <li>site map</li>
      <li>contact</li>
      <li>fashion</li>
      <li>fitness</li>
      <li>feelings</li>
    </ul>
    <div class="social" aria-label="Social media links">
      <span></span><span></span><span></span><span></span><span></span><span></span>
    </div>
    <div class="copyright">© 2018 Kite and Compass All Rights Reserved</div>
  </footer>
</div>
</body>
</html>
```